Q.B.Y 'Qafilat Bin Yusr' for General Transportation

this company is a Iraqi based company.
It provides a number of logistics activities such as;
Overland Transportation
High and heavy logistics
Customs clearance
warehousing
Automotive logistics
The company has been registered since 2009.
If you have any other questions please feel free to ask.
Target Market(s)
Automotive
White goods
All Trading sectors
Industry/Entity Type
Automotive

```html
<!DOCTYPE html>
<html lang="en">
<head>
<meta charset="utf-8">
<title>Qafilat Bin Yusr Transportation</title>
<link rel="stylesheet" href="https://fonts.googleapis.com/css2?family=PT+Sans:ital,wght@0,400;0,700;1,400&family=Oswald:wght@300&display=swap">
<style>
:root{
  --navy:#0c2e60;
  --navy-line:#1d4279;
  --sky:#7fb0e8;
  --link-blue:#2a8fd6;
  --page:#f2f2f2;
  --band:#dadada;
  --ink:#4a4a4a;
  --ink-soft:#777;
  --white:#fff;
}
*{margin:0;padding:0;box-sizing:border-box}
html,body{width:1200px;height:1070px;overflow:hidden}
body{position:relative;background:var(--page);font-family:"PT Sans",sans-serif;color:var(--ink)}
.abs{position:absolute}

.topbar{left:0;top:0;width:1200px;height:26px;background:var(--band)}
.topbar .phone-icon{left:714px;top:3px}
.topbar .contact{left:738px;top:2px;font-size:9.5px;line-height:11px;color:#888}
.topbar .contact strong{color:#666}
.topbar .contact b{color:var(--link-blue);font-weight:400}

.brand{left:217px;top:48px}
.brand .mark{font-size:46px;font-weight:700;color:var(--navy);line-height:44px;letter-spacing:1px}
.brand .name{margin-left:40px;font-size:11.5px;color:var(--navy);line-height:12px;margin-top:4px}
.brand .sub{margin-left:40px;font-size:11.5px;color:#999;line-height:12px}

.tagline{left:802px;top:59px;width:167px;height:37px;background:var(--navy);border-radius:3px;overflow:hidden}
.tagline .truck{left:0;top:0;width:64px;height:37px;background:linear-gradient(135deg,#3f7fd0,#1c4b93 60%,#0c2e60)}
.tagline p{left:62px;top:8px;width:82px;text-align:center;font-size:9.5px;line-height:10px;color:#9cc8f5}
.tagline svg{position:absolute;right:8px;top:11px}

.nav{left:217px;top:140px;width:752px;height:39px;background:var(--navy);border-radius:5px 5px 0 0;display:flex;align-items:center;padding-left:28px}
.nav a{font-size:9.5px;color:var(--white);text-decoration:none;text-transform:uppercase}
.nav a.current{color:var(--sky)}
.nav span{color:var(--white);font-size:10px;margin:0 23px}

.hero{left:0;top:179px;width:1200px;height:304px;background:linear-gradient(90deg,#4a4a55 0%,#8a8a98 25%,#bdbdc8 55%,#a9a9b8 80%,#7a7a88 100%)}
.hero-text{right:231px;top:292px;display:flex;flex-direction:column;align-items:flex-end;gap:4px}
.hero-text .lead{background:var(--white);color:var(--navy);font-size:15.5px;font-weight:700;padding:6px 4px 6px 7px;line-height:23px}
.hero-text .item{background:var(--white);color:var(--navy);font-size:12.5px;padding:2px 4px 2px 9px;line-height:15.5px;margin-top:3px}

.featured{left:217px;top:483px;width:752px;height:255px;background:var(--navy);border-radius:0 0 5px 5px}
.featured h2{position:absolute;left:25px;top:28px;font-family:"Oswald",sans-serif;font-weight:300;font-size:19px;color:var(--sky);text-transform:uppercase;letter-spacing:.3px}
.service{position:absolute;top:74px;width:170px}
.service h3{font-weight:400;font-size:19px;line-height:22px;color:var(--white);height:58px}
.service p{font-size:9px;line-height:11px;color:#79a6dd;margin-top:9px;width:160px}
.service .more{display:inline-block;margin-top:25px;background:#f2f2f2;color:#555;font-size:8px;padding:6px 10px;text-decoration:none}
.divider{position:absolute;top:78px;width:1px;height:160px;background:var(--navy-line)}

.column{top:783px}
.column h4{font-size:12.5px;font-weight:400;color:var(--navy);text-transform:uppercase;margin-bottom:12px}
.column h4 em{font-style:normal;font-size:15px}
.column .intro{font-size:9px;line-height:11.5px;font-weight:700;color:#666}
.column p{font-size:9px;line-height:11.5px;color:var(--ink-soft)}
.column a.cont{font-size:9px;font-style:italic;color:#666;text-decoration:underline}
.event{border-bottom:1px solid #ccc;padding-bottom:12px;margin-bottom:12px;width:182px}
.event time{display:block;font-size:7.5px;font-style:italic;color:var(--link-blue);margin-bottom:6px}
.event p{font-size:7.5px;line-height:11px}
.others-photo{width:232px;height:92px;border-radius:4px;margin:10px 0 18px;background:linear-gradient(180deg,#9bb7d4 0%,#d6dde4 45%,#9a9c9e 75%,#6d6f70 100%)}

.footer{left:0;top:1009px;width:1200px;height:61px;background:var(--band)}
.footer .f-brand{position:absolute;left:217px;top:18px;display:flex;align-items:center;gap:14px}
.footer .f-brand .mark{font-size:22px;font-weight:700;color:var(--navy)}
.footer .f-brand div{font-size:7.5px;line-height:8px;color:var(--navy)}
.footer .f-brand div span{color:#999}
.footer .f-nav{position:absolute;left:397px;top:22px;font-size:7px;color:#777}
.footer .f-nav a{color:#777;text-decoration:none}
.footer .f-nav a.current{color:var(--navy)}
.footer .f-nav small{display:block;margin-top:6px;font-size:7px}
.footer .follow{position:absolute;left:738px;top:21px;font-size:16px;color:#bbb;text-transform:uppercase;letter-spacing:.5px}
.footer .sep{position:absolute;left:834px;top:6px;width:1px;height:32px;background:#bbb}
.footer .social{position:absolute;left:851px;font-size:7.5px;color:#999;display:flex;align-items:center;gap:8px}
.footer .social i{display:block;width:14px;height:14px;border-radius:50%}
</style>
</head>
<body>

<header class="abs topbar">
  <svg class="abs phone-icon" width="20" height="20" viewBox="0 0 20 20"><circle cx="10" cy="10" r="10" fill="#888"/><path d="M7 5c1 0 1.5 2 1.5 2.5S7.5 8.5 7.5 9c.5 1.5 2 3 3.5 3.5.5 0 1-1 1.5-1s2.5.5 2.5 1.5-1 2-2 2C9 15 5 11 5 7c0-1 1-2 2-2z" fill="#fff"/></svg>
  <div class="abs contact"><strong>We're here for you</strong><br>Phone <b>1.200.555.0100</b> (U.S.) | International <b>+1.555.010.0199</b></div>
</header>

<div class="abs brand">
  <div class="mark">Q.B.Y</div>
  <div class="name">Qafilat Bin Yusr</div>
  <div class="sub">Transportation</div>
</div>

<div class="abs tagline">
  <div class="abs truck" role="img" aria-label="Photo of a blue transport truck"></div>
  <p class="abs">TRANSPORTATION SHOULD BE</p>
  <svg width="14" height="14" viewBox="0 0 14 14"><path d="M2 1l5 6-5 6M7 1l5 6-5 6" stroke="#3d77c2" stroke-width="2" fill="none"/></svg>
</div>

<nav class="abs nav">
  <a class="current" href="#">Home</a><span>|</span>
  <a href="#">About Us</a><span>|</span>
  <a href="#">Services</a><span>|</span>
  <a href="#">Transportation</a><span>|</span>
  <a href="#">Contact Us</a>
</nav>

<section class="abs hero" role="img" aria-label="Photo of a blue truck with a white trailer driving along a city street, motion blurred"></section>
<div class="abs hero-text">
  <div class="lead">We Provides a number of Logistics Activities</div>
  <div class="item">Overland Transportation</div>
  <div class="item">High and heavy logistics</div>
  <div class="item">Customs clearance</div>
  <div class="item">Warehousing</div>
  <div class="item">Automotive logistics</div>
</div>

<section class="abs featured">
  <h2>Featured Services</h2>
  <div class="service" style="left:25px">
    <h3>Overland<br>Transportation</h3>
    <p>Lorem ipsum dolor sit amet, consectetur adipisicing elit, sed do eiusmod tempor incididunt ut labore et dolore magna aliqua. Ut enim ad minim veniam</p>
    <a class="more" href="#">READ MORE &gt;&gt;</a>
  </div>
  <div class="divider" style="left:190px"></div>
  <div class="service" style="left:215px">
    <h3>High &amp; Heavy<br>Logistics</h3>
    <p>Lorem ipsum dolor sit amet, consectetur adipisicing elit, sed do eiusmod tempor incididunt ut labore et dolore magna aliqua. Ut enim ad minim veniam</p>
    <a class="more" href="#">READ MORE &gt;&gt;</a>
  </div>
  <div class="divider" style="left:380px"></div>
  <div class="service" style="left:396px">
    <h3>Automotive<br>Logistics</h3>
    <p>Lorem ipsum dolor sit amet, consectetur adipisicing elit, sed do eiusmod tempor incididunt ut labore et dolore magna aliqua. Ut enim ad minim veniam</p>
    <a class="more" href="#">READ MORE &gt;&gt;</a>
  </div>
  <div class="divider" style="left:564px"></div>
  <div class="service" style="left:582px">
    <h3>Customs<br>Clearance</h3>
    <p>Lorem ipsum dolor sit amet, consectetur adipisicing elit, sed do eiusmod tempor incididunt ut labore et dolore magna aliqua. Ut enim ad minim veniam</p>
    <a class="more" href="#">READ MORE &gt;&gt;</a>
  </div>
</section>

<section class="abs column" style="left:217px;width:240px">
  <h4><em>Welcome</em> to our company</h4>
  <p class="intro">Lorem ipsum dolor sit amet, consectetur adipisicing elit, sed do eiusmod tempor incididunt ut labore et dolore magna aliqua. Ut enim ad minim veniam</p>
  <p style="margin:12px 0 20px">Quis nostrud exercitation ullamco laboris nisi ut aliquip ex ea commodo consequat. Duis aute irure dolor in reprehenderit in voluptate velit esse cillum dolore eu fugiat nulla pariatur. Excepteur sint occaecat cupidatat non proident, sunt in culpa qui officia deserunt mollit anim id est laborum.</p>
  <a class="cont" href="#">continue &gt;&gt;</a>
</section>

<section class="abs column" style="left:513px;width:190px">
  <h4>Company Events</h4>
  <div class="event"><time>11 February 2014</time><p>Lorem ipsum dolor sit amet, consectetur adipisicing elit, sed do eiusmod tempor incididunt ut labore et dolore magna aliqua. Ut enim ad minim veniam</p></div>
  <div class="event"><time>11 February 2014</time><p>Lorem ipsum dolor sit amet, consectetur adipisicing elit, sed do eiusmod tempor incididunt ut labore et dolore magna aliqua. Ut enim ad minim veniam</p></div>
  <a class="cont" href="#">all events &gt;&gt;</a>
</section>

<section class="abs column" style="left:738px;width:232px">
  <h4>Others</h4>
  <p class="intro">Lorem ipsum dolor sit amet, consectetur adipisicing elit, sed do eiusmod tempor incididunt ut labore et dolore magna aliqua. Ut enim ad minim veniam</p>
  <div class="others-photo" role="img" aria-label="Photo of a car carrier truck loaded with vehicles"></div>
  <a class="cont" href="#">continue &gt;&gt;</a>
</section>

<footer class="abs footer">
  <div class="f-brand">
    <span class="mark">Q.B.Y</span>
    <div>Qafilat Bin Yusr<br><span>Transportation</span></div>
  </div>
  <div class="f-nav">
    <a class="current" href="#">HOME</a> &nbsp;|&nbsp; <a href="#">ABOUT US</a> &nbsp;|&nbsp; <a href="#">SERVICES</a> &nbsp;|&nbsp; <a href="#">TRANSPORTATION</a> &nbsp;|&nbsp; <a href="#">CONTACT US</a>
    <small>All Right Reserved 2014.</small>
  </div>
  <div class="follow">Follow Us</div>
  <div class="sep"></div>
  <div class="social" style="top:10px"><i style="background:#3b5a9a"></i>Find Us on Facelink</div>
  <div class="social" style="top:27px"><i style="background:#3fa9e8"></i>Tweet in Chirper</div>
</footer>

</body>
</html>
```